Wordpress Design Project - IT Consulting Services Web Site

Our are starting a new technology services company. We will provide services in software implementation and business intelligence.

We need a beautiful Wordpress web site design. We need a design for the homepage, and one interior content page.

The site must have a very professional and polished look and feel. What I have suggested below are things that I think work, but I am not a designer and I am open to your professional opinions. Please be willing to use your best judgment.

The homepage should have the following elements:
- A Header Area that includes:
o The company logo, and
o navigation (consistent with the interior page)
o a social media link section that includes rss feeds, youtube, facebook, linkedin and tweets
- A Body that includes:
o A slider
o An area that features up to six of the most recent or important posts including a thumbnail and small picture, a title, and a short excerpt for each.
o An area for around 100 words of text and an image
- A footer that includes:
o The company logo
o Contact information

The interior page is relatively simple. It should include the same navigation element as the homepage, and accommodate a one column text layout.

The current site …
You can visit the current site at www.korvelpath.com I built the current site using the “Velthor Quick Pane” premium theme. If you visit this site you get a sense of some of the things I am talking about, but there are things that I do not like about the current site. Here’s what I like and what I don’t like.

What I like about the current site:
- It is reactive – it adapts to the size of the viewing browser
- It has a “metro” feel to it. The company will have an association with Microsoft and having a “metro” theme is a plus, but not a requirement.
- It is different without being hard to navigate – the site the slider is from the “glide cascade widget”, the posts are represented with tiles and rearrange themselves when a topic is selected.

What I don’t like:
- The site lacks a cohesive feel – it feels to me like a bunch of different elements without a single theme that pulls everything together.
- It is not aesthetically appealing to me.
- The tiles in the post section are too big.
- I don’t like the white background – I would prefer a background color and ideally a background that somehow incorporates the graphic in the logo.

About themes
As I said, I used a Velthor theme in my design. I will be happy to continue using this theme, or would be willing to buy a new premium theme, so long as the cost is less than $100 U.S.

Site Map:
What we do
ERP Implementation
Business Intelligence
Who we are
What’s different about us
Principles
Mission, Vision, Values
Actions
How we work
What’s Different About Us
Blogs
What Papers
Presentations
Join
What we are looking for
What are you looking for?
Benefits
Context
Updates

Regarding Pictures
Please do not feel you need to use any of the pictures currently on the site.  Use whatever pictures you feel look best.  Comps are okay. 

It is not necessary to use any of the content on the current site - you do not need to use either the pictures or the text.  Please feel free to use pictures of your choice (comps okay), and/or lorem text.

The top level navigation is the navigation I would like.

Hello all,

Since this is a Wordpress project, it goes without saying I will need to implement this design in Wordpress.  It is not absolutely necessary that a design that matches an existing template (free or not), but a design that does will have an advantage over a design which requires that a new template be coded from scratch.

Thank you.

Target Market(s)

Business executives and potential employees

Industry/Entity Type

Software

Requirements
Nice to have
• It would be nice if the site was reactive.

```html
<!DOCTYPE html>
<html lang="en">
<head>
<meta charset="utf-8">
<title>Korvel Path – Home</title>
<link href="https://fonts.googleapis.com/css2?family=Arimo:ital,wght@0,400;0,700;1,400&display=swap" rel="stylesheet">
<style>
:root{
  --top-bar:#0b6aa3;
  --sky:#0c88cc;
  --sky-light:#23a3e3;
  --nav:#1d9de2;
  --nav-dark:#0f7fc0;
  --panel-head:#1676ad;
  --panel-bg:#f2f3f5;
  --link:#1a8ad4;
  --text:#333;
  --muted:#555;
  --footer:#0aa1e2;
  --footer-bar:#0577b1;
  --white:#fff;
  --red:#c8261c;
  --photo-grey:#9aa7b2;
}
*{box-sizing:border-box;margin:0;padding:0}
html,body{width:960px;height:1200px;overflow:hidden}
body{font-family:"Arimo",Arial,sans-serif;color:var(--text);font-size:10px;position:relative;
  background:linear-gradient(#fff 0,#fff 115px,#d8dadd 160px,var(--sky) 162px,var(--sky) 430px,#1a92d4 432px,#3aa8e2 1017px)}
.abs{position:absolute}
.top-bar{left:0;top:0;width:960px;height:17px;background:var(--top-bar)}
.top-bar a{position:absolute;top:2px;color:var(--white);font-size:10px;text-decoration:none}
.brand{left:158px;top:76px;font-size:30px;color:#3b3f44;letter-spacing:-.5px;font-weight:400}
.social{top:30px;width:19px;height:19px;border-radius:3px}
.search{left:689px;top:28px;width:134px;height:24px;background:var(--white);border:1px solid #c9ced3;border-radius:3px;font-size:9px;color:#777;padding:6px 8px;font-style:italic}
.main-nav{left:429px;top:92px;width:396px;height:31px;display:flex;background:linear-gradient(var(--sky-light),var(--nav-dark));border-radius:3px;box-shadow:0 3px 6px rgba(0,0,0,.25)}
.main-nav a{flex:auto;color:var(--white);font-size:12px;text-align:center;line-height:31px;text-decoration:none;border-right:1px solid rgba(255,255,255,.35)}
.main-nav a:last-child{border:0}
.content-sheet{left:130px;top:148px;width:703px;height:847px;background:var(--white);border-radius:4px;box-shadow:0 0 8px rgba(0,0,0,.3)}
.slider-area{left:130px;top:148px;width:703px;height:270px;background:#eef0f2;border-radius:4px 4px 0 0}
.slide{left:141px;top:162px;width:681px;height:238px;background:linear-gradient(100deg,#f3f4f5 0,#d9dde1 45%,var(--photo-grey) 75%,#6d7b86 100%)}
.quote{left:160px;top:176px;width:340px;font-size:17px;line-height:23px;color:#222}
.quote-by{left:333px;top:266px;font-size:11px;font-style:italic;color:var(--red)}
.arrow{top:262px;width:26px;height:42px;background:var(--white);box-shadow:0 0 3px rgba(0,0,0,.3)}
.dots{left:452px;top:418px;display:flex;gap:3px}
.dots span{width:12px;height:12px;border-radius:50%;border:1px solid #999;background:var(--white)}
.dots span.on{background:var(--red);border-color:#999}
.tile{top:446px;width:216px;height:184px;background:var(--panel-bg);border:1px solid #cfd3d7;border-radius:3px}
.tile h2{height:25px;background:linear-gradient(#2289c4,var(--panel-head));color:var(--white);font-size:11px;font-weight:400;text-align:center;line-height:25px;border-radius:3px 3px 0 0}
.tile .pic{margin:8px 6px 0;height:90px}
.tile ul{list-style:none;margin:10px 0 0 8px;font-size:9.5px;line-height:12px;color:#333}
.tile li::before{content:"";display:inline-block;border-left:5px solid var(--link);border-top:3px solid transparent;border-bottom:3px solid transparent;margin-right:6px}
.photo{background:linear-gradient(135deg,#c9b9a6,#8a7f78 50%,#cfd5da)}
.welcome-pic{left:143px;top:675px;width:176px;height:172px}
.welcome{left:335px;top:670px;width:270px;font-size:10px;line-height:13px;color:var(--muted)}
.welcome h3{font-size:10px;font-weight:400;color:#333;text-transform:uppercase}
.welcome h3 b{color:var(--link);font-weight:400}
.welcome h4{font-size:10px;font-weight:400;color:var(--link)}
.welcome .gap{height:13px}
.blog{left:620px;top:647px;width:205px;height:337px;background:var(--panel-bg);border:1px solid #d2d5d9}
.blog-head{height:24px;border-bottom:1px solid #d2d5d9;padding:7px 8px;font-size:9.5px;color:#444;display:flex;justify-content:space-between}
.blog-head a{color:var(--red);font-size:9px;text-decoration:underline}
.post{height:52px;border-bottom:1px solid #dcdfe2;display:flex;align-items:center;padding:0 8px;gap:10px}
.post:last-child{border:0}
.post .thumb{width:36px;height:30px;flex:none}
.post p{font-size:8.5px;line-height:11px;color:#555}
.post p b{color:#222}
.testimonials{left:143px;top:899px;width:257px;height:85px;border:1px solid #cfd3d7;background:var(--panel-bg)}
.testimonials h5{position:absolute;left:10px;top:7px;font-size:9.5px;font-weight:400;color:#333}
.testimonials .face{position:absolute;left:18px;top:24px;width:36px;height:42px;background:linear-gradient(#b3a497,#6d6863)}
.testimonials blockquote{position:absolute;left:78px;top:24px;width:170px;font-size:11px;line-height:14px;font-style:italic;color:#333}
.testimonials cite{position:absolute;left:104px;top:69px;font-size:8px;font-style:normal;color:var(--link)}
.newsletter{left:408px;top:899px;width:203px;height:85px;background:linear-gradient(#1275ae,#0a5f96);color:var(--white)}
.newsletter h5{position:absolute;left:12px;top:7px;font-size:10px;font-weight:400}
.newsletter p{position:absolute;left:12px;top:26px;font-size:9px}
.newsletter .field{position:absolute;left:12px;top:49px;width:125px;height:22px;background:var(--white);border-radius:3px}
.newsletter .btn{position:absolute;left:132px;top:48px;width:60px;height:24px;background:linear-gradient(var(--sky-light),var(--nav-dark));border:1px solid #9fd3f2;border-radius:3px;font-size:10px;text-align:center;line-height:22px}
.footer{left:0;top:1017px;width:960px;height:162px;background:var(--footer);color:var(--white)}
.footer h6{position:absolute;top:12px;font-size:10px;font-weight:700}
.footer .rule{position:absolute;left:152px;top:29px;width:680px;height:1px;background:rgba(255,255,255,.45)}
.footer ul{position:absolute;left:165px;top:34px;list-style:none;font-size:9px;line-height:11.5px}
.footer .about{position:absolute;left:267px;top:34px;width:150px;font-size:9px;line-height:11.5px}
.footer .more{position:absolute;left:348px;top:126px;width:52px;height:12px;border-radius:6px;background:var(--white);color:#333;font-size:7.5px;text-align:center;line-height:12px}
.footer .pin-box{position:absolute;left:443px;top:34px;width:38px;height:38px;background:#f29a1f}
.footer address{position:absolute;left:500px;top:34px;font-size:9px;line-height:11.5px;font-style:normal}
.footer .input{position:absolute;left:628px;width:108px;height:18px;background:var(--white);border:1px solid #8ccbef;color:#444;font-size:8px;padding:3px 6px}
.footer .send{position:absolute;left:749px;top:146px;width:56px;height:13px;border-radius:6px;background:#0c4f78;font-size:8px;text-align:center;line-height:13px}
.copyright{left:0;top:1179px;width:960px;height:21px;background:var(--footer-bar);color:var(--white);font-size:9.5px;text-align:center;line-height:21px}
</style>
</head>
<body>
<div class="abs top-bar"><a style="left:744px">Login</a><a style="left:781px">Help</a></div>

<div class="abs brand">KorvelPath</div>

<div class="abs social" style="left:594px;background:#3b5998"></div>
<div class="abs social" style="left:616px;background:#33b5e8"></div>
<div class="abs social" style="left:638px;background:#1c75b5"></div>
<div class="abs social" style="left:660px;background:#f08a1c"></div>
<div class="abs search">Search
  <svg class="abs" style="left:112px;top:4px" width="14" height="14" viewBox="0 0 14 14"><circle cx="6" cy="6" r="4.2" fill="none" stroke="#1a8ad4" stroke-width="2"/><line x1="9" y1="9" x2="13" y2="13" stroke="#1a8ad4" stroke-width="2.4"/></svg>
</div>

<nav class="abs main-nav"><a>HOME</a><a>ABOUT US</a><a>SERVICES</a><a>BLOG</a><a>JOIN</a><a>CONTACT US</a></nav>

<div class="abs content-sheet"></div>
<div class="abs slider-area"></div>
<div class="abs slide" role="img" aria-label="Slide photo: veteran baseball manager in cap and jersey sitting in a stadium dugout"></div>
<p class="abs quote">"Baseball is a simple game.<br>&nbsp;If you have good players and if you keep<br>&nbsp;them in the right frame of mind then the<br>&nbsp;manager is a success."</p>
<p class="abs quote-by">Rusty Calloway</p>
<svg class="abs arrow" style="left:141px;border-radius:0 21px 21px 0" viewBox="0 0 26 42"><polyline points="15,14 8,21 15,28" fill="none" stroke="#333" stroke-width="2.5"/></svg>
<svg class="abs arrow" style="left:796px;border-radius:21px 0 0 21px" viewBox="0 0 26 42"><polyline points="11,14 18,21 11,28" fill="none" stroke="#333" stroke-width="2.5"/></svg>
<div class="abs dots"><span class="on"></span><span></span><span></span><span></span></div>

<section class="abs tile" style="left:140px"><h2>WHO WE ARE</h2><div class="pic photo" role="img" aria-label="Photo: group of smiling business people"></div>
<ul><li>What's different about us.</li><li>Principles</li><li>Mission, Vission, Values</li></ul></section>
<section class="abs tile" style="left:370px"><h2>WHAT WE DO</h2><div class="pic photo" role="img" aria-label="Photo: team meeting around a table"></div>
<ul><li>ERP Implementation</li><li>Business intelligence</li></ul></section>
<section class="abs tile" style="left:606px"><h2>HOW WE WORKS</h2><div class="pic photo" role="img" aria-label="Photo: presenter at a whiteboard with colleagues"></div>
<ul><li>What's different about us.</li><li>Blogs</li><li>What papers</li><li>Presentations</li></ul></section>

<div class="abs welcome-pic photo" role="img" aria-label="Photo: three colleagues reviewing a folder together"></div>
<article class="abs welcome">
  <h3>Welcome to <b>KORVELPATH.com</b></h3>
  <div class="gap"></div>
  <h3 style="font-weight:700">People processes and tools</h3>
  <h4>Putting People first</h4>
  <p>Every services firm is made up people, processes and tools. At Korvel Path we put people first, tailoring everything we do find, hire, train, and keep the very best people. Because once you have the best people everything else will follows.</p>
  <div class="gap"></div>
  <h3>KORVEL PATH</h3>
  <h4>What's The Idea?</h4>
  <p>The idea is an old one but a great one. Edwin Harlow Marsh was an "American Dream". It's the idea that your success should depend on your ability and achievements, not on where you started out. It's an idea we try to live up to.</p>
</article>

<aside class="abs blog">
  <div class="blog-head"><span>RECENT BLOG POSTS</span><a>View All</a></div>
  <div class="post"><div class="thumb photo" role="img" aria-label="Post thumbnail"></div><p><b>Lorem ipsum dolor,</b><br>Lorem ipsum dolor sit amet,conse ctetuer adipiscing elit....</p></div>
  <div class="post"><div class="thumb photo" role="img" aria-label="Post thumbnail"></div><p><b>Lorem ipsum dolor,</b><br>Lorem ipsum dolor sit amet,conse ctetuer adipiscing elit....</p></div>
  <div class="post"><div class="thumb photo" role="img" aria-label="Post thumbnail"></div><p><b>Lorem ipsum dolor,</b><br>Lorem ipsum dolor sit amet,conse ctetuer adipiscing elit....</p></div>
  <div class="post"><div class="thumb photo" role="img" aria-label="Post thumbnail"></div><p><b>Lorem ipsum dolor,</b><br>Lorem ipsum dolor sit amet,conse ctetuer adipiscing elit....</p></div>
  <div class="post"><div class="thumb photo" role="img" aria-label="Post thumbnail"></div><p><b>Lorem ipsum dolor,</b><br>Lorem ipsum dolor sit amet,conse ctetuer adipiscing elit....</p></div>
  <div class="post"><div class="thumb photo" role="img" aria-label="Post thumbnail"></div><p><b>Lorem ipsum dolor,</b><br>Lorem ipsum dolor sit amet,conse ctetuer adipiscing elit....</p></div>
</aside>

<section class="abs testimonials">
  <h5>TESTIMONIALS</h5>
  <svg class="abs" style="left:236px;top:9px" width="14" height="7" viewBox="0 0 14 7"><polygon points="0,3.5 5,0 5,7" fill="#333"/><polygon points="14,3.5 9,0 9,7" fill="#333"/></svg>
  <div class="face" role="img" aria-label="Portrait of the client giving the testimonial"></div>
  <blockquote>"Lorem ipsum dolor sit amet, consectetur adipiscing elit set diem nonumy"</blockquote>
  <cite>Dale Morrow, CEO of BRX, Lakeview</cite>
</section>

<section class="abs newsletter">
  <h5>NEWSLETTER</h5>
  <p>Receive our update to your email, weekly.</p>
  <div class="field"></div>
  <div class="btn">SUBMIT</div>
</section>

<footer class="abs footer">
  <h6 style="left:165px">Main menu</h6>
  <h6 style="left:267px">About Us</h6>
  <h6 style="left:440px">Get In Touch</h6>
  <h6 style="left:627px">Contact Us</h6>
  <div class="rule"></div>
  <ul><li>Home</li><li>About Us</li><li>Services</li><li>Blog</li><li>Join</li><li>Terms of Use</li><li>Privacy Policy</li><li>Contact Us</li></ul>
  <p class="about">Korvel provides technology services in variety of areas. What makes us different is our focus on finding, training and retaining the very best people who focus on pro viding our customers with the very best services.</p>
  <div class="more">read more</div>
  <div class="pin-box"><svg width="38" height="38" viewBox="0 0 38 38"><circle cx="19" cy="19" r="12" fill="none" stroke="#fff" stroke-width="2"/><path d="M19 11a5 5 0 0 0-5 5c0 4 5 10 5 10s5-6 5-10a5 5 0 0 0-5-5z" fill="#fff"/><circle cx="19" cy="16" r="1.8" fill="#f29a1f"/></svg></div>
  <address>Address :<br>418 Linden Pkwy,<br>Ashford, MN<br>USA</address>
  <div class="input" style="top:35px">Name</div>
  <div class="input" style="top:59px">E-mail</div>
  <div class="input" style="top:81px;width:178px;height:57px"></div>
  <div class="send">SEND</div>
</footer>
<div class="abs copyright">Copyright © 2013, KorvelPath.com. All rights reserved.</div>
</body>
</html>
```